Landing Page - #1 Social Media Training

I need a landing page where i'm going to sell the number one social media for small business package. Hopefully i can use this template for others.

The themes are in oranges.

See www.tavuvkip.com

Its a dogs breakfast.

I need high end, good looking, kova/trindlepay/logos.
Would love a wordpress design but i could slice it into one if it wasn't.

Need room for feature bullet points, a video preview, and text along the bottom... Want it in oranges and whites like the packaging with social media along the top... Side bar on the right for opt-in box, left side copy etc.

Target Market(s)

The audience is small and medium businesses.

Industry/Entity Type

Small Business

Requirements
Must have
• Opt-in
headline
footer

```html
<!DOCTYPE html>
<html lang="en">
<head>
<meta charset="utf-8">
<title>Summit Online – Campfold 101</title>
<link href="https://fonts.googleapis.com/css2?family=Arimo:ital,wght@0,400;0,700;1,400&family=Luckiest+Guy&display=swap" rel="stylesheet">
<style>
:root{
  --orange:#f7791f;
  --orange-light:#fbb040;
  --orange-deep:#f26a10;
  --text:#333;
  --muted:#8a8a8a;
  --panel:#f0f0f0;
  --band:#e4e4e4;
  --white:#fff;
  --dark:#2c2c2c;
}
*{margin:0;padding:0;box-sizing:border-box}
html,body{width:1137px;height:1200px;overflow:hidden;background:var(--white)}
body{position:relative;font-family:"Arimo",Arial,sans-serif;color:var(--text)}
.abs{position:absolute}

.hero-bg{left:0;top:0;width:1137px;height:435px}
.brand{left:74px;top:40px;display:flex;align-items:center;gap:14px;color:var(--orange);font-weight:700;font-size:44px;letter-spacing:-1px;white-space:nowrap}
.brand-dot{width:26px;height:26px;border-radius:50%;background:var(--orange)}

.nav{left:694px;top:42px;height:34px;display:flex;background:linear-gradient(#4a4a4a,#1e1e1e);border-radius:5px;box-shadow:0 2px 4px rgba(0,0,0,.35)}
.nav a{color:var(--white);text-decoration:none;font-size:15px;line-height:34px;padding:0 19px;border-left:1px solid #555;white-space:nowrap}
.nav a:first-child{border-left:0;color:var(--orange-light)}

.hero-title{left:12px;top:254px;width:270px;text-align:center;font-family:"Luckiest Guy",Impact,sans-serif;color:var(--white);text-shadow:2px 2px 3px rgba(120,50,0,.6);white-space:nowrap}
.hero-title .l1{font-size:30px;line-height:34px}
.hero-title .l2{font-size:21px;line-height:28px;margin-top:12px}
.hero-title .l3{font-size:30px;line-height:34px}

.product-box{left:284px;top:193px;width:142px;height:233px;background:linear-gradient(100deg,#e8e8e8,#fff 40%,#f3f3f3);box-shadow:4px 6px 10px rgba(0,0,0,.25)}
.buy-btn{left:453px;top:330px;width:143px;height:45px;background:linear-gradient(#4a4a4a,#222);border-radius:4px;color:var(--white);font-size:18px;display:flex;align-items:center;gap:10px;padding-left:12px;box-shadow:0 2px 4px rgba(0,0,0,.4);white-space:nowrap}
.buy-btn svg{flex:none}

.video{left:669px;top:132px;width:434px;height:285px;background:#111;border-radius:5px;padding:6px;box-shadow:0 3px 8px rgba(0,0,0,.4)}
.video-frame{position:relative;width:100%;height:240px;background:linear-gradient(135deg,#6b6b6b,#d9d9d9 55%,#f4f4f4)}
.video-title{position:absolute;left:0;top:0;width:100%;height:30px;background:rgba(0,0,0,.7);color:var(--white);font-size:14px;line-height:30px;padding-left:8px;white-space:nowrap;overflow:hidden}
.video-play{position:absolute;left:190px;top:112px}
.video-bar{height:27px;display:flex;align-items:center;gap:14px;padding-left:10px;color:#aaa;font-size:10px}

.tagline{left:0;top:435px;width:1137px;height:82px;background:var(--band);text-align:center;font-style:italic;font-size:24px;line-height:82px;color:var(--muted)}

.photo{left:17px;top:538px;width:146px;height:144px;border:2px solid #cfcfcf;border-radius:4px;background:linear-gradient(135deg,#f6a14a,#3a3f55 55%,#dcdcdc)}
.h-orange{color:var(--orange);font-size:19px;font-weight:400;white-space:nowrap}
.about-title{left:181px;top:543px}
.about-copy{left:178px;top:578px;width:453px;font-size:13.5px;line-height:25.5px;text-align:justify;color:#444}

.features{left:18px;top:706px;width:608px;height:247px;background:var(--panel);border-radius:6px}
.features-title{left:23px;top:22px;font-size:18px}
.features-sub{left:24px;top:62px;font-size:18px;font-weight:700;color:var(--muted);white-space:nowrap}
.bullets{list-style:none;font-size:15px;line-height:32.5px;white-space:nowrap}
.bullets li{position:relative;padding-left:18px}
.bullets li::before{content:"";position:absolute;left:0;top:12px;border-left:6px solid #333;border-top:4px solid transparent;border-bottom:4px solid transparent}
.f-col1{left:47px;top:100px}
.f-col2{left:322px;top:100px}

.awards-title{left:653px;top:543px}
.awards-art{left:659px;top:580px;width:461px;height:116px;background:linear-gradient(90deg,#d9d9d9,#f7f7f7 30%,#c9b68a 45%,#f7f7f7 60%,#cfcfcf 80%,#f7f7f7)}
.a-list{list-style:none;font-size:14px;line-height:30px;color:#444;white-space:nowrap}
.a-list li{position:relative;padding-left:16px}
.a-list li::before{content:"›";position:absolute;left:0;top:0;font-weight:700;color:#333}
.a-col1{left:664px;top:722px}
.a-col2{left:914px;top:722px}

.lower{left:0;top:978px;width:1137px;height:157px;background:var(--panel)}
.divider{top:15px;width:2px;height:125px;background:#c8c8c8}
.lower h3{position:absolute;font-size:18px;font-weight:400;color:#222;top:15px;white-space:nowrap}
.badge{left:17px;top:57px;width:74px;height:74px;border-radius:50%;background:radial-gradient(circle at 40% 35%,#fff3a0,#e2b52b 70%,#b8871b);color:#3b4f8c;font-size:13px;font-weight:700;display:flex;align-items:center;justify-content:center}
.cards{left:114px;top:85px;display:flex;gap:3px}
.cards span{width:36px;height:21px;background:var(--white);border:1px solid #9a9a9a;font-size:6.5px;line-height:19px;text-align:center;color:#333;box-shadow:1px 1px 2px rgba(0,0,0,.3);white-space:nowrap}
.social{left:342px;top:79px;display:flex;gap:12px}
.social span{width:37px;height:37px;border-radius:50%;background:#2e5aa3;color:var(--white);font-size:8px;display:flex;align-items:center;justify-content:center}
.social span:nth-child(2){background:#2aa6e0}
.social span:nth-child(4){background:#333}
.social span:nth-child(6){background:var(--orange)}
.field-label{font-size:14px;color:#444;text-align:right;width:120px;white-space:nowrap}
.field{width:201px;height:35px;background:var(--white);border:1px solid #ccc;box-shadow:inset 0 2px 3px rgba(0,0,0,.12)}
.subscribe{left:1016px;top:100px;width:101px;height:32px;background:linear-gradient(#4a4a4a,#222);color:var(--white);font-size:15px;line-height:32px;text-align:center}

.footer{left:0;top:1135px;width:1137px;height:65px;background:linear-gradient(var(--orange-light),var(--orange))}
.copyright{left:26px;top:26px;font-size:12px;color:#222;white-space:nowrap}
.footer-links{right:22px;top:26px;font-size:12px;color:#222;word-spacing:2px;white-space:nowrap}
</style>
</head>
<body>

<svg class="abs hero-bg" viewBox="0 0 1137 435" aria-hidden="true">
  <defs>
    <linearGradient id="heroGrad" x1="0" y1="0" x2="1" y2="1">
      <stop offset="0" stop-color="#f68b1f"/>
      <stop offset=".5" stop-color="#fbab3a"/>
      <stop offset="1" stop-color="#f57c1c"/>
    </linearGradient>
  </defs>
  <path d="M0 171 H395 C430 171 440 105 485 105 H1137 V435 H0 Z" fill="url(#heroGrad)"/>
</svg>

<div class="abs brand"><span class="brand-dot"></span>Summit Online</div>

<nav class="abs nav">
  <a href="#">Home</a>
  <a href="#">About Dean Marlow</a>
  <a href="#">Contact Us</a>
</nav>

<div class="abs hero-title">
  <div class="l1">SUMMIT ONLINE</div>
  <div class="l2">CAMPFOLD 101</div>
  <div class="l3">SOL FOR SMB</div>
</div>

<div class="abs product-box" role="img" aria-label="Product box for the Campfold 101 course pack"></div>

<div class="abs buy-btn">
  <svg width="26" height="26" viewBox="0 0 26 26"><circle cx="13" cy="13" r="11" fill="none" stroke="#aaa" stroke-width="2"/><path d="M7 13h10M13 8l5 5-5 5" stroke="#ddd" stroke-width="2" fill="none"/></svg>
  BUY NOW
</div>

<div class="abs video">
  <div class="video-frame" role="img" aria-label="Video preview of the presenter introducing the course">
    <div class="video-title">(SOL for SMB) Summit OnLine - Campfold 101 for...</div>
    <svg class="video-play" width="56" height="40" viewBox="0 0 56 40"><rect width="56" height="40" rx="6" fill="rgba(0,0,0,.7)"/><path d="M22 11l14 9-14 9z" fill="#fff"/></svg>
  </div>
  <div class="video-bar">
    <svg width="12" height="12" viewBox="0 0 12 12"><path d="M2 1l9 5-9 5z" fill="#aaa"/></svg>
    <span>0:00 / 6:38</span>
  </div>
</div>

<div class="abs tagline">Social Media &amp; Internet Marketing for Today's Small to Medium Business</div>

<div class="abs photo" role="img" aria-label="Portrait photo of Dean Marlow"></div>
<h2 class="abs h-orange about-title">About Dean Marlow</h2>
<p class="abs about-copy">The standard chunk of Lorem Ipsum used since the 1500s is reproduced below for those interested. Sections 1.10.32 and 1.10.33 from "de Finibus Bonorum et Malorum" by Cicero are also reproduced in their exact original form, accompanied.</p>

<section class="abs features">
  <h2 class="abs h-orange features-title">Features</h2>
  <p class="abs features-sub">One easy system to help grow your business Online!</p>
  <ul class="abs bullets f-col1">
    <li>Search Engine Marketing</li>
    <li>Social Media Marketing</li>
    <li>Social Network Marketing</li>
    <li>Geo - Targeted Marketing</li>
  </ul>
  <ul class="abs bullets f-col2">
    <li>Applications</li>
    <li>Social Tools</li>
    <li>Community Development</li>
  </ul>
</section>

<h2 class="abs h-orange awards-title">Awards the product has won</h2>
<div class="abs awards-art" role="img" aria-label="Row of award trophies the product has won"></div>
<ul class="abs a-list a-col1">
  <li>2 Tallis Awards</li>
  <li>4 Pixora Awards</li>
  <li>3 Dovan Awards</li>
  <li>1 Media Achievement Award</li>
  <li>2 OVA Awards</li>
  <li>1 DX Award</li>
  <li>2 Conveyor Awards</li>
  <li>2 MarVo Awards</li>
</ul>
<ul class="abs a-list a-col2">
  <li>1 Zenith Award</li>
  <li>2 Arnie's (Arnold Rivers)</li>
  <li>1 Astra Award</li>
  <li>1 Helios Creative Award</li>
  <li>1 MerVox Award</li>
  <li>1 Flexa Gold Award</li>
</ul>

<section class="abs lower">
  <h3 style="left:23px">Payments:</h3>
  <div class="abs badge">Pagora</div>
  <div class="abs cards"><span>kova</span><span>Dyscor</span><span>trindlepay</span><span>Amerlo</span><span>Chequo</span></div>
  <div class="abs divider" style="left:322px"></div>

  <h3 style="left:342px">Connect with us:</h3>
  <div class="abs social"><span>Fribo</span><span>Chirpa</span><span>Delvo</span><span>Gorma</span><span>Mynest</span><span>Feed</span></div>
  <div class="abs divider" style="left:640px"></div>

  <h3 style="left:664px">News Letter</h3>
  <label class="abs field-label" style="left:665px;top:60px">Username :</label>
  <div class="abs field" style="left:796px;top:51px"></div>
  <label class="abs field-label" style="left:665px;top:107px">E- mail Address :</label>
  <div class="abs field" style="left:796px;top:98px"></div>
  <div class="abs subscribe">Subscribe</div>
</section>

<footer class="abs footer">
  <p class="abs copyright">Copyright © 2011 www.tavuvkip.com All rights reserved</p>
  <p class="abs footer-links">Press Room &nbsp;|&nbsp; SOL Info &nbsp;|&nbsp; Affiliates &nbsp;|&nbsp; Privacy Policy &nbsp;|&nbsp; Terms and Conditions</p>
</footer>

</body>
</html>
```